Lark IT Support company needs a flyer

This flyer will be delivered by hand to prospective customers in a door drop campaign.
Double sided A6
We support SMEs in Central London mainly Lark networks. We also supply managed services including email and internet connectivity.
The target audience is office managers, receptionists and business owners.
It will be extremely simple and illustration mainly.
Any ideas are welcome but we quite like the following:
A text poster saying
"Make IT easy" or something like that.
An illustration of two people, the client and us. Us juggling web, IT etc and the Client able to concentrate on their job.
Copy is being written by a professional copywriter, content of which will depend on the flyer design.
Target Market(s)
Small SMEs using Pomelo Lark computers, design companies, agencies etc.
Industry/Entity Type
Technical Service
Requirements
Must have
- Our number - 0203 555 0184
- Our email - info@quill-node.it
- Our web address - www.quill-node.it
Nice to have
- Some clever eye catching designs
Should not have
- Too much text
- Overly complicated design

```html
<!DOCTYPE html>
<html lang="en">
<head>
<meta charset="utf-8">
<title>QuillNode – Our Services</title>
<link href="https://fonts.googleapis.com/css2?family=Ubuntu:wght@400;500;700&display=swap" rel="stylesheet">
<style>
  :root {
    --olive: #8a9e22;
    --olive-dark: #4d5a0a;
    --lime: #d2e25c;
    --lime-light: #e6ecc4;
    --paper: #e9e9e9;
    --ink: #141414;
    --white: #ffffff;
    --sky-deep: #2c5f8e;
    --sky-mid: #6e93b5;
    --sky-pale: #d3dbe2;
    --footer: #4f5a1a;
  }
  * { margin: 0; padding: 0; box-sizing: border-box; }
  html, body { width: 851px; height: 1200px; overflow: hidden; }
  body { font-family: "Ubuntu", sans-serif; color: var(--ink); }
  .flyer {
    position: relative; width: 851px; height: 1200px; overflow: hidden;
    background: linear-gradient(180deg, var(--paper) 0%, var(--paper) 36%, var(--lime-light) 50%, var(--lime) 72%, var(--lime) 100%);
  }
  .backdrop { position: absolute; inset: 0; }
  .top-email {
    position: absolute; top: 21px; right: 31px;
    font-size: 19px; font-weight: 500; color: var(--white);
  }
  .brand-tab {
    position: absolute; top: 57px; left: 17px;
    font-size: 35px; font-weight: 700; color: var(--ink); letter-spacing: -0.5px;
  }
  .seal-name {
    position: absolute; top: 566px; left: 48px; width: 290px; text-align: center;
    font-size: 44px; font-weight: 700; color: var(--olive);
  }
  .services-title {
    position: absolute; top: 712px; left: 0; width: 851px; text-align: center;
    font-size: 40px; font-weight: 700; color: var(--olive-dark);
  }
  .service {
    position: absolute; width: 280px; text-align: center;
    font-size: 21px; color: var(--ink);
  }
  .service svg { display: block; margin: 0 auto 12px; width: 52px; height: 52px; fill: var(--ink); }
  .col-1 { left: 16px; } .col-2 { left: 293px; } .col-3 { left: 570px; }
  .row-1 { top: 762px; } .row-2 { top: 888px; } .row-3 { top: 1012px; }
  .footer {
    position: absolute; top: 1168px; left: 0; width: 851px; text-align: center;
    font-size: 14.5px; color: var(--footer);
  }
  .footer .footer-link { font-size: 17px; font-weight: 500; }
</style>
</head>
<body>
<main class="flyer">
  <svg class="backdrop" width="851" height="1200" viewBox="0 0 851 1200">
    <defs>
      <linearGradient id="sky" x1="0" y1="0" x2="1" y2="1">
        <stop offset="0" stop-color="#8fb3cf"/>
        <stop offset="0.25" stop-color="var(--sky-deep)"/>
        <stop offset="0.55" stop-color="var(--sky-mid)"/>
        <stop offset="1" stop-color="var(--sky-pale)"/>
      </linearGradient>
      <radialGradient id="glow" cx="0.3" cy="0.55" r="0.45">
        <stop offset="0" stop-color="#e4ecf2" stop-opacity="0.55"/>
        <stop offset="1" stop-color="#e4ecf2" stop-opacity="0"/>
      </radialGradient>
      <filter id="soft" x="-5%" y="-5%" width="110%" height="110%">
        <feGaussianBlur stdDeviation="6"/>
      </filter>
    </defs>
    <rect class="top-band" x="0" y="0" width="851" height="72" fill="var(--olive)"/>
    <path class="brand-tab-shape" d="M0 0 H270 Q245 72 230 120 Q220 136 200 136 H0 Z" fill="var(--olive)"/>
    <circle class="seal" cx="224" cy="516" r="194" fill="#efefef" stroke="var(--olive)" stroke-width="10"/>
    <path class="hero-glow" d="M46 96 H804 V656 Q600 640 420 600 Q200 550 46 418 Z" fill="none" stroke="var(--white)" stroke-width="10" filter="url(#soft)"/>
    <g class="hero-photo" role="img" aria-label="Hand reaching towards a stream of floating photo frames against a blue sky">
      <path d="M46 96 H804 V656 Q600 640 420 600 Q200 550 46 418 Z" fill="url(#sky)"/>
      <path d="M46 96 H804 V656 Q600 640 420 600 Q200 550 46 418 Z" fill="url(#glow)"/>
    </g>
  </svg>

  <div class="top-email">info@quill-node.it</div>
  <div class="brand-tab">QuillNode</div>
  <div class="seal-name">QuillNode</div>

  <h1 class="services-title">Our Services</h1>

  <div class="service col-1 row-1">
    <svg viewBox="0 0 52 52"><circle cx="26" cy="26" r="23" fill="none" stroke="var(--ink)" stroke-width="5"/><circle cx="26" cy="26" r="14" fill="none" stroke="var(--ink)" stroke-width="3"/><path d="M14 20 L32 13 M38 18 L30 36 M36 36 L16 34 M14 30 L22 14" stroke="var(--ink)" stroke-width="3"/></svg>
    IT Support
  </div>
  <div class="service col-2 row-1">
    <svg viewBox="0 0 52 52"><path d="M12 44 A10 10 0 0 1 10 24 A14 14 0 0 1 36 18 A12 12 0 0 1 42 44 Z"/><path d="M26 24 L19 32 H23 V42 H29 V32 H33 Z" fill="var(--white)"/></svg>
    CLOUD BASED BACKUP
  </div>
  <div class="service col-3 row-1">
    <svg viewBox="0 0 52 52"><path d="M12 44 A10 10 0 0 1 10 24 A14 14 0 0 1 36 18 A12 12 0 0 1 42 44 Z"/><text x="26" y="35" text-anchor="middle" font-size="18" font-weight="700" fill="var(--white)" font-family="Ubuntu, sans-serif">@</text></svg>
    CLOUD BASED EMAIL
  </div>

  <div class="service col-1 row-2">
    <svg viewBox="0 0 52 52"><circle cx="34" cy="14" r="9"/><path d="M22 40 Q24 26 34 26 Q46 26 48 40 Z"/><circle cx="18" cy="20" r="10" stroke="var(--white)" stroke-width="2"/><path d="M2 48 Q4 32 18 32 Q32 32 34 48 Z" stroke="var(--white)" stroke-width="2"/></svg>
    IT CONSULTANCY
  </div>
  <div class="service col-2 row-2">
    <svg viewBox="0 0 52 52"><circle cx="26" cy="26" r="22" fill="none" stroke="var(--ink)" stroke-width="5"/><circle cx="26" cy="26" r="13" fill="none" stroke="var(--ink)" stroke-width="5"/><circle cx="26" cy="26" r="5"/><rect x="20" y="30" width="12" height="22" fill="var(--lime)"/></svg>
    INTERNET CONNECTIVITY
  </div>
  <div class="service col-3 row-2">
    <svg viewBox="0 0 52 52"><path d="M2 26 Q26 4 50 26 Q26 48 2 26 Z"/><circle cx="26" cy="26" r="10" fill="var(--lime)"/><circle cx="26" cy="26" r="6"/><circle cx="23" cy="23" r="2" fill="var(--lime)"/></svg>
    MONITORING
  </div>

  <div class="service col-1 row-3">
    <svg viewBox="0 0 52 52"><path d="M6 10 H30 V15 H11 V41 H37 V24 H42 V46 H6 Z"/><path d="M40 4 L48 12 L26 34 L16 36 L18 26 Z"/></svg>
    IT PROJECT MANAGEMENT
  </div>
  <div class="service col-2 row-3">
    <svg viewBox="0 0 52 52"><path d="M4 16 L16 6 V12 H46 V20 H16 V26 Z"/><path d="M48 36 L36 26 V32 H6 V40 H36 V46 Z"/></svg>
    RELOCATION
  </div>
  <div class="service col-3 row-3">
    <svg viewBox="0 0 52 52"><path d="M12 2 H40 L46 14 L34 24 H18 L6 14 Z"/><circle cx="26" cy="36" r="14"/><path d="M22 10 H30 L26 18 Z" fill="var(--lime)"/></svg>
    SPAM PREVATION
  </div>

  <footer class="footer">12 - 16 Marlow Lane, London SE1 4QX – 0203 555 0184 – <span class="footer-link">info@quill-node.it</span> – <span class="footer-link">www.quill-node.it</span></footer>
</main>
</body>
</html>
```